rt for guide - bartholomew finch personal speaking/consulting website

custom website for my personal speaking/consulting services brand, you can see the basic site we are using as a placeholder at www.rtforguide.example now. I want to re-position this to more of a personal brand site and have video samples of speaking events, downloadable content, a video blog, and links to podcast. I really like the design of dorianwelk.example and the feature set should be fairly similar to his. I'll begin to compile more stock images etc. to use for sliders like he has done, for now we'll need to use stock imagery or existing photography from my social accounts. You can get a feel for social at all platforms/bfinchbroker i.e. facebook.com/bfinchbroker. the site should be primarily geared toward showcasing speaking/consulting services and content, as well as be flexible to allow for additional downloadables etc. in the future.

Target Market(s)

entrepreneurs and leaders looking to grow themselves, their business, and those they lead.

Coding

Coded - Design and coding required

Number of Pages Required

3 page

Font styles to use
Sans Serif

Colors

Designer to choose colors to be used in the design.

Requirements
Must have
• modern slick design, video blog, podcast feed, registration for people to subscribe to newsletter

```html
<!DOCTYPE html>
<html lang="en">
<head>
<meta charset="utf-8">
<title>Bartholomew Finch — Personal Speaking & Consulting</title>
<link rel="stylesheet" href="https://fonts.googleapis.com/css2?family=Montserrat:ital,wght@0,400;0,500;0,600;0,700;1,800&family=Lato:wght@400;700&display=swap">
<style>
:root{
  --red:#ed1c24;
  --red-dark:#c8141b;
  --ink:#222;
  --text:#444;
  --grey-bg:#f1f1f1;
  --line:#e0a5a7;
  --footer:#14161c;
  --white:#fff;
}
*{box-sizing:border-box;margin:0;padding:0}
html,body{width:1200px;height:5213px;overflow:hidden;background:var(--white)}
body{position:relative;font-family:"Lato",sans-serif;color:var(--text)}
.abs{position:absolute}
.h-title{font-family:"Montserrat",sans-serif;font-weight:600;color:var(--red);font-size:38px;line-height:1.1}
.underline{position:absolute;height:4px;background:var(--red)}
.lorem{font-size:13px;line-height:26px;color:var(--text)}

/* header */
.header{top:0;left:0;width:1200px;height:108px;background:var(--white)}
.brand{left:108px;top:36px;font-family:"Montserrat",sans-serif;font-weight:700;font-size:32px;color:var(--ink);letter-spacing:.5px}
.brand span{color:var(--red)}
.contact{top:38px;display:flex;align-items:center;gap:12px;font-size:15px;color:#555}
.icon-box{width:34px;height:34px;border:2px solid var(--red);display:flex;align-items:center;justify-content:center}
.nav{top:108px;left:0;width:1200px;height:64px;background:var(--red);display:flex;justify-content:center;align-items:center;gap:58px;padding-left:40px}
.nav a{color:var(--white);text-decoration:none;font-family:"Montserrat",sans-serif;font-weight:500;font-size:19px}

/* hero */
.hero{top:172px;left:0;width:1200px;height:610px;background:linear-gradient(180deg,#8a8d93 0%,#4a4c52 45%,#1e1f24 100%)}
.hero-title{left:110px;top:392px;font-family:"Montserrat",sans-serif;font-style:italic;font-weight:800;font-size:52px;line-height:74px;color:var(--white)}
.circle-btn{width:50px;height:50px;border-radius:50%;background:var(--red);display:flex;align-items:center;justify-content:center}

/* about */
.about-text{left:112px;top:920px;width:520px}
.btn{background:var(--red);color:var(--white);font-family:"Montserrat",sans-serif;font-weight:600;display:flex;align-items:center;justify-content:center}

/* leaders */
.leaders{top:1278px;left:0;width:1200px;height:420px;background:var(--grey-bg)}
.leaders h2{position:absolute;top:96px;width:100%;text-align:center;font-family:"Montserrat",sans-serif;font-weight:500;font-size:30px;color:var(--ink)}
.leaders p{position:absolute;top:156px;left:220px;width:760px;text-align:center;font-family:"Montserrat",sans-serif;font-size:15px;line-height:27px;color:#444}

/* podcast */
.podcast{top:1698px;left:0;width:1200px;height:660px;background:linear-gradient(180deg,#e8e8e8,#d4d4d4)}
.pod-card{position:absolute;top:1870px;width:300px}
.pod-img{width:300px;height:285px;position:relative}
.pod-tag{position:absolute;left:0;top:0;width:50px;height:50px;background:var(--red);display:flex;align-items:center;justify-content:center}
.pod-card p{margin-top:14px;padding-left:6px;font-size:16px;line-height:26px;color:#333}

/* books */
.books-title{top:2418px;width:1200px;text-align:center}
.books-box{left:112px;top:2560px;width:976px;height:226px;border:2px solid var(--red)}
.books-box p{position:absolute;left:36px;top:36px;width:672px;font-size:13.5px;line-height:25px}
.download{position:absolute;left:790px;top:40px;width:104px;text-align:center;font-family:"Montserrat",sans-serif;font-weight:600;font-size:17px;color:#444}

/* videos */
.videos{top:2924px;left:0;width:1200px;height:560px;background:var(--grey-bg)}
.vid{position:absolute;top:3105px;width:316px;height:214px;border:2px solid #e57a7e;padding:6px;background:var(--white)}
.vid-img{width:100%;height:100%;position:relative;display:flex;align-items:center;justify-content:center}
.play{width:58px;height:36px;background:var(--red);border-radius:8px;display:flex;align-items:center;justify-content:center}
.vid-cap{position:absolute;top:3346px;width:316px;text-align:center;font-size:15.5px;line-height:30px;color:#333}
.sq-arrow{width:36px;height:30px;border:2px solid var(--red);display:flex;align-items:center;justify-content:center;background:var(--white)}

/* services */
.svc{position:absolute;top:3672px;width:292px;height:288px;border:2px solid #d93a40;padding:4px;border-radius:4px}
.svc-img{width:100%;height:100%}
.svc-label{position:absolute;top:4000px;width:292px;text-align:center;font-family:"Montserrat",sans-serif;font-weight:500;font-size:20px;color:#333}

/* newsletter */
.news{top:4070px;left:0;width:1200px;height:152px;background:linear-gradient(90deg,#ec8d95 0%,#d6577a 55%,#a83f84 100%)}
.news h3{position:absolute;left:224px;top:56px;font-family:"Montserrat",sans-serif;font-weight:600;font-size:31px;color:var(--white)}
.news-form{position:absolute;left:690px;top:48px;width:368px;height:54px;background:var(--white);border-radius:27px}
.news-form span{position:absolute;left:34px;top:18px;font-size:15px;color:#666}
.news-form b{position:absolute;right:4px;top:4px;width:136px;height:46px;border-radius:23px;background:var(--red);color:var(--white);font-family:"Montserrat",sans-serif;font-weight:600;font-size:15px;display:flex;align-items:center;justify-content:center}

/* quote */
.quote-title{top:4290px;width:1200px;text-align:center}
.field-label{position:absolute;font-family:"Montserrat",sans-serif;font-size:18px;color:#333}
.field-line{position:absolute;height:1px;background:var(--line)}

/* footer */
.footer{top:4830px;left:0;width:1200px;height:352px;background:var(--footer)}
.f-text{position:absolute;font-family:"Montserrat",sans-serif;color:var(--white);font-size:16px}
.f-links{position:absolute;left:718px;top:4922px;font-family:"Montserrat",sans-serif;color:var(--white);font-size:16px;line-height:34px}
.social{position:absolute;left:940px;width:30px;height:22px;font-family:"Montserrat",sans-serif;font-size:9px;font-weight:600;color:var(--white);border:1px solid var(--white);display:flex;align-items:center;justify-content:center}
.bottom{top:5182px;left:0;width:1200px;height:31px;background:var(--red)}
.bottom span{position:absolute;top:9px;font-family:"Montserrat",sans-serif;font-size:11px;color:var(--white)}
</style>
</head>
<body>

<!-- Header -->
<header class="abs header">
  <div class="abs brand">BARTHOLOMEW <span>FINCH</span></div>
  <div class="abs contact" style="left:668px">
    <div class="icon-box"><svg width="18" height="13" viewBox="0 0 18 13"><rect x="0" y="0" width="18" height="13" fill="#222"/><path d="M0 0 L9 7 L18 0" stroke="#fff" stroke-width="1.5" fill="none"/></svg></div>
    bartholomewfinch.example
  </div>
  <div class="abs contact" style="left:926px">
    <div class="icon-box"><svg width="18" height="18" viewBox="0 0 24 24"><path d="M6.6 10.8a15.2 15.2 0 0 0 6.6 6.6l2.2-2.2c.3-.3.7-.4 1-.2 1.1.4 2.3.6 3.6.6.6 0 1 .4 1 1V20c0 .6-.4 1-1 1A17 17 0 0 1 3 4c0-.6.4-1 1-1h3.5c.6 0 1 .4 1 1 0 1.3.2 2.5.6 3.6.1.3 0 .7-.2 1z" fill="#222"/></svg></div>
    888 888 8888
  </div>
</header>
<nav class="abs nav">
  <a>START HERE</a><a>ABOUT</a><a>PODCAST</a><a>STORE</a><a>EVENTS</a><a>CONTACT US</a>
</nav>

<!-- Hero -->
<section class="abs hero" role="img" aria-label="Group photo of a team in formal wear at an awards event"></section>
<svg class="abs" style="left:0;top:690px" width="1200" height="100" viewBox="0 0 1200 100" preserveAspectRatio="none">
  <path d="M0 60 Q360 110 760 70 Q1000 45 1200 60 L1200 100 L0 100Z" fill="#fff"/>
  <path d="M500 90 Q900 60 1200 55 L1200 75 Q900 78 620 98Z" fill="#ed1c24"/>
</svg>
<h1 class="abs hero-title">Personal<br>Speaking &amp; Consulting</h1>
<div class="abs circle-btn" style="left:37px;top:438px"><svg width="22" height="22" viewBox="0 0 24 24"><path d="M20 12H5M11 5l-7 7 7 7" stroke="#fff" stroke-width="3" fill="none"/></svg></div>
<div class="abs circle-btn" style="left:1100px;top:438px"><svg width="22" height="22" viewBox="0 0 24 24"><path d="M4 12h15M13 5l7 7-7 7" stroke="#fff" stroke-width="3" fill="none"/></svg></div>

<!-- About -->
<h2 class="abs h-title" style="left:110px;top:850px">About Me</h2>
<div class="underline" style="left:112px;top:896px;width:76px;height:3px"></div>
<p class="abs lorem about-text">Lorem ipsum dolor sit amet, consectetur adipiscing elit, sed do eiusmod tempor incididunt ut labore et dolore magna aliqua. Quis ipsum suspendisse ultrices gravida. Risus commodo viverra maecenas accumsan lacus vel facilisisLorem ipsum dolor sit amet, consectetur adipiscing elit, sed do eiusmod tempor incididunt ut labore et dolore magna aliqua. Quis ipsum suspendisse ultrices gravida. Risus commodo viverra maecenas accumsan lacus vel facilisis.</p>
<div class="abs btn" style="left:112px;top:1112px;width:148px;height:52px;font-size:15px">READ MORE&nbsp;<svg width="16" height="14" viewBox="0 0 16 14"><path d="M2 2l5 5-5 5M9 2l5 5-5 5" stroke="#fff" stroke-width="2.4" fill="none"/></svg></div>
<svg class="abs" style="left:740px;top:858px" width="290" height="320" viewBox="0 0 290 320">
  <path d="M160 290 A152 152 0 0 1 40 60" stroke="#ed1c24" stroke-width="6" fill="none"/>
  <circle cx="165" cy="150" r="145" fill="#fff"/>
</svg>
<div class="abs" role="img" aria-label="Portrait of the speaker smiling" style="left:770px;top:865px;width:266px;height:300px;border-radius:50% 50% 46% 46%;background:radial-gradient(circle at 50% 45%,#c99a7c 0%,#7a5340 55%,#2a2220 100%)"></div>

<!-- Wedge -->
<svg class="abs" style="left:0;top:1208px" width="1200" height="72" viewBox="0 0 1200 72"><path d="M0 0 L560 70 L0 72Z" fill="#ed1c24"/></svg>

<!-- Leaders -->
<section class="abs leaders">
  <h2>The place where entrepreneurs come to become leaders.</h2>
  <p>Bartholomew Finch and Marcus Delane swap their secrets on how to polish your leadership skills, shift your business mindset,and empower your team. Subscribe to this blog to get the latest tips and tricks to help you be a successful entrepreneur.</p>
  <div class="btn" style="position:absolute;left:474px;top:264px;width:294px;height:72px;font-size:18px">Subscribe to our Podcast</div>
</section>

<!-- Podcast -->
<section class="abs podcast" role="img" aria-label="Faded background photo of a pickup truck under a canopy"></section>
<svg class="abs" style="left:0;top:1698px" width="1200" height="660" viewBox="0 0 1200 660">
  <path d="M640 0 L1200 0 L1200 62Z" fill="#ed1c24"/>
  <path d="M0 575 L0 660 L790 660Z" fill="#ed1c24"/>
</svg>
<h2 class="abs h-title" style="left:106px;top:1774px">Podcast Feed</h2>
<div class="underline" style="left:108px;top:1826px;width:84px;height:3px"></div>

<div class="pod-card" style="left:110px">
  <div class="pod-img" role="img" aria-label="Selfie of two people outdoors" style="background:linear-gradient(135deg,#b89570,#6f5440)">
    <div class="pod-tag"><svg width="18" height="26" viewBox="0 0 18 26"><rect x="5" y="1" width="8" height="15" rx="4" fill="#fff"/><path d="M2 12a7 7 0 0 0 14 0M9 19v5M5 24h8" stroke="#fff" stroke-width="2" fill="none"/></svg></div>
  </div>
  <p>Lorem ipsum dolor sit amet, consectetur adipiscing elit, sed do</p>
</div>
<div class="pod-card" style="left:446px">
  <div class="pod-img" role="img" aria-label="Cocktail glass on a table" style="background:linear-gradient(135deg,#b9c4cc,#3b4a58 60%,#a36a2a)">
    <div class="pod-tag"><svg width="18" height="26" viewBox="0 0 18 26"><rect x="5" y="1" width="8" height="15" rx="4" fill="#fff"/><path d="M2 12a7 7 0 0 0 14 0M9 19v5M5 24h8" stroke="#fff" stroke-width="2" fill="none"/></svg></div>
  </div>
  <p>Lorem ipsum dolor sit amet, consectetur adipiscing elit, sed do</p>
</div>
<div class="pod-card" style="left:780px">
  <div class="pod-img" role="img" aria-label="Concert stage with purple lights and crowd" style="background:linear-gradient(135deg,#5b2a8a,#b04aa8 50%,#1c1030)">
    <div class="pod-tag"><svg width="18" height="26" viewBox="0 0 18 26"><rect x="5" y="1" width="8" height="15" rx="4" fill="#fff"/><path d="M2 12a7 7 0 0 0 14 0M9 19v5M5 24h8" stroke="#fff" stroke-width="2" fill="none"/></svg></div>
  </div>
  <p>Lorem ipsum dolor sit amet, consectetur adipiscing elit, sed do</p>
</div>
<svg class="abs" style="left:570px;top:2276px" width="76" height="22" viewBox="0 0 76 22">
  <circle cx="12" cy="11" r="8" fill="none" stroke="#ed1c24" stroke-width="2"/>
  <circle cx="38" cy="11" r="9" fill="#ed1c24"/>
  <circle cx="64" cy="11" r="8" fill="#ed1c24"/>
</svg>

<!-- Books -->
<h2 class="abs h-title books-title">Books, Podcast,<br>Courses &amp; More</h2>
<div class="underline" style="left:474px;top:2514px;width:138px;height:3px"></div>
<div class="abs books-box">
  <p>Lorem ipsum dolor sit amet, consectetur adipiscing elit, sed do eiusmod tempor incididunt ut labore et dolore magna aliqua. Quis ipsum suspendisse ultrices gravida. Risus commodo viverra maecenas accumsan lacus vel facilisis. Lorem ipsum dolor sit amet, consectetur adipiscing elit, sed do eiusmod tempor incididunt ut labore et dolore magna aliqua. Quis ipsum suspendisse ultrices gravida. Risus commodo viverra maecenas accumsan lacus vel facilisis.</p>
  <div class="download">
    <svg width="100" height="90" viewBox="0 0 100 90"><rect x="3" y="3" width="94" height="84" rx="8" fill="none" stroke="#ed1c24" stroke-width="5"/><path d="M50 20v38M36 45l14 14 14-14" stroke="#222" stroke-width="3.5" fill="none"/><path d="M28 52v14h44V52" stroke="#222" stroke-width="3.5" fill="none"/></svg>
    <div style="margin-top:10px">Download</div>
  </div>
</div>

<!-- Videos -->
<svg class="abs" style="left:0;top:2848px" width="1200" height="78" viewBox="0 0 1200 78"><path d="M0 0 L570 76 L0 78Z" fill="#ed1c24"/></svg>
<section class="abs videos"></section>
<h2 class="abs h-title" style="top:3010px;width:1200px;text-align:center">Videos</h2>
<div class="underline" style="left:562px;top:3062px;width:80px;height:3px"></div>
<div class="vid" style="left:106px"><div class="vid-img" role="img" aria-label="Speaker recording a video indoors" style="background:linear-gradient(135deg,#6a6a66,#3a3330)"><div class="play"><svg width="16" height="18" viewBox="0 0 16 18"><path d="M2 1l13 8-13 8z" fill="#fff"/></svg></div></div></div>
<div class="vid" style="left:444px"><div class="vid-img" role="img" aria-label="Small white dog on grass" style="background:linear-gradient(135deg,#6f9a4a,#c9c4b6 55%,#4d7a34)"><div class="play"><svg width="16" height="18" viewBox="0 0 16 18"><path d="M2 1l13 8-13 8z" fill="#fff"/></svg></div></div></div>
<div class="vid" style="left:780px"><div class="vid-img" role="img" aria-label="Presenter at a whiteboard in a training room" style="background:linear-gradient(135deg,#e4e6ea,#9aa0a8 60%,#5a5048)"><div class="play"><svg width="16" height="18" viewBox="0 0 16 18"><path d="M2 1l13 8-13 8z" fill="#fff"/></svg></div></div></div>
<div class="vid-cap" style="left:96px">Lorem ipsum dolor sit amet, consectetur adipiscing elit, sed do eiusmod tempor</div>
<div class="vid-cap" style="left:444px">Lorem ipsum dolor sit amet, consectetur adipiscing elit, sed do eiusmod tempor</div>
<div class="vid-cap" style="left:782px">Lorem ipsum dolor sit amet, consectetur adipiscing elit, sed do eiusmod tempor</div>
<div class="abs sq-arrow" style="left:42px;top:3196px"><svg width="16" height="14" viewBox="0 0 16 14"><path d="M15 7H2M7 2L2 7l5 5" stroke="#ed1c24" stroke-width="2" fill="none"/></svg></div>
<div class="abs sq-arrow" style="left:1112px;top:3196px"><svg width="16" height="14" viewBox="0 0 16 14"><path d="M1 7h13M9 2l5 5-5 5" stroke="#ed1c24" stroke-width="2" fill="none"/></svg></div>
<svg class="abs" style="left:0;top:3484px" width="1200" height="64" viewBox="0 0 1200 64"><path d="M640 0 L1200 0 L1200 62Z" fill="#ed1c24"/></svg>

<!-- Services -->
<h2 class="abs h-title" style="left:110px;top:3578px">Services</h2>
<div class="underline" style="left:112px;top:3630px;width:94px;height:3px"></div>
<div class="svc" style="left:110px"><div class="svc-img" role="img" aria-label="Woman in red dress speaking on stage" style="background:linear-gradient(180deg,#8fc6d6,#d46a5a 55%,#3a2522)"></div></div>
<div class="svc" style="left:462px"><div class="svc-img" role="img" aria-label="Man building a tepee frame with party streamers" style="background:linear-gradient(180deg,#d9d6cf,#b9845a 60%,#6a5a4a)"></div></div>
<div class="svc" style="left:812px"><div class="svc-img" role="img" aria-label="Team gathered in an office for a group photo" style="background:linear-gradient(180deg,#d4d6d8,#7e7670 60%,#4a4440)"></div></div>
<div class="svc-label" style="left:110px">Leadership Skills</div>
<div class="svc-label" style="left:462px">Entrepreneurs</div>
<div class="svc-label" style="left:812px">Team Building</div>

<!-- Newsletter -->
<section class="abs news">
  <svg style="position:absolute;left:132px;top:52px" width="62" height="46" viewBox="0 0 62 46"><rect x="1" y="1" width="60" height="44" rx="3" fill="#fff"/><path d="M2 3 L31 26 L60 3" stroke="#e57a8a" stroke-width="3" fill="none"/><path d="M2 44 L24 22M60 44 L38 22" stroke="#e57a8a" stroke-width="2" fill="none"/></svg>
  <h3>Subscribe To Newsletter</h3>
  <div class="news-form"><span>Enter Email Address</span><b>SUBSCRIBE</b></div>
</section>

<!-- Express Quote -->
<h2 class="abs h-title quote-title" style="font-size:34px">Express Quote</h2>
<div class="underline" style="left:564px;top:4338px;width:72px;height:3px"></div>
<div class="abs" style="left:0;top:4368px;width:74px;height:428px;background:var(--red)"></div>
<div class="abs" style="left:186px;top:4380px;font-family:'Montserrat',sans-serif;font-weight:600;font-size:19px;color:var(--red)">Basic Details</div>
<div class="field-label" style="left:194px;top:4456px">Name:</div>
<div class="field-line" style="left:314px;top:4476px;width:224px"></div>
<div class="field-label" style="left:648px;top:4456px">Last Name:</div>
<div class="field-line" style="left:774px;top:4476px;width:226px"></div>
<div class="field-label" style="left:196px;top:4544px">Tel:</div>
<div class="field-line" style="left:314px;top:4564px;width:224px"></div>
<div class="field-label" style="left:648px;top:4544px">Email:</div>
<div class="field-line" style="left:774px;top:4564px;width:226px"></div>
<div class="field-label" style="left:194px;top:4628px">Message:</div>
<div class="field-line" style="left:314px;top:4648px;width:696px"></div>
<div class="abs btn" style="left:872px;top:4724px;width:138px;height:46px;font-size:16px">SUBMIT</div>

<!-- Footer -->
<section class="abs footer" role="img" aria-label="Dark photo of a vehicle interior behind the footer"></section>
<svg class="abs" style="left:0;top:4800px" width="1200" height="70" viewBox="0 0 1200 70" preserveAspectRatio="none">
  <path d="M0 0 L1200 0 L1200 30 Q700 10 0 48Z" fill="#fff"/>
  <path d="M0 48 Q700 12 1200 30 L1200 40 Q700 24 0 62Z" fill="#ed1c24"/>
</svg>
<div class="abs" style="left:116px;top:4934px;font-family:'Montserrat',sans-serif;font-weight:700;font-size:22px;color:#fff">BARTHOLOMEW <span style="color:var(--red)">FINCH</span></div>
<svg class="abs" style="left:414px;top:4924px" width="16" height="22" viewBox="0 0 16 22"><path d="M8 1a7 7 0 0 0-7 7c0 5 7 13 7 13s7-8 7-13a7 7 0 0 0-7-7z" fill="#fff"/><circle cx="8" cy="8" r="3" fill="#14161c"/></svg>
<div class="f-text" style="left:448px;top:4924px;line-height:20px">Lorem ipsum dolor sit<br>amet, consectetur adipi</div>
<svg class="abs" style="left:414px;top:5006px" width="18" height="18" viewBox="0 0 24 24"><path d="M6.6 10.8a15.2 15.2 0 0 0 6.6 6.6l2.2-2.2c.3-.3.7-.4 1-.2 1.1.4 2.3.6 3.6.6.6 0 1 .4 1 1V20c0 .6-.4 1-1 1A17 17 0 0 1 3 4c0-.6.4-1 1-1h3.5c.6 0 1 .4 1 1 0 1.3.2 2.5.6 3.6.1.3 0 .7-.2 1z" fill="#fff"/></svg>
<div class="f-text" style="left:450px;top:5006px">Tel: (555) 010-4477</div>
<svg class="abs" style="left:414px;top:5056px" width="20" height="14" viewBox="0 0 20 14"><rect width="20" height="14" fill="#fff"/><path d="M0 0L10 8 20 0" stroke="#14161c" stroke-width="1.5" fill="none"/></svg>
<div class="f-text" style="left:450px;top:5052px">info@bartholomewfinch.example</div>
<div class="f-links">Start Here<br>About<br>Podcast<br>Store<br>Events<br>Contact us</div>
<div class="social" style="top:4928px">Page</div>
<div class="social" style="top:4970px">Feed</div>
<div class="social" style="top:5012px">Circle</div>
<div class="social" style="top:5054px">Work</div>
<div class="social" style="top:5096px">Video</div>
<footer class="abs bottom">
  <span style="left:118px">© 2019 All Rights Reserved | Privacy Policy | Terms and Conditions</span>
  <span style="left:1128px">C36</span>
</footer>

</body>
</html>
```